Web form face-lift for an online startup

We are a web startup building a SaaS application for the freight industry. The project is mainly dedicated to the paint the main form that our customer are using along the search results that the they get. All details are in the attached documents.
Updates
The application serves the Freight Forwarders community so please think towards this industry when using background images, banners, colors, icons, etc. Computer and technology images are irrelevant.
Customer fields at the top of the page is actually part of the form.
Target Market(s)
Usually business users (Sales people, procurement, shippers, freight forwarders). Some are less tech savvy and some appreciate the new trendy web apps.
Industry/Entity Type
Building
Colors
Designer to choose colors to be used in the design.
Look and feel
Each slider illustrates characteristics of the customer's brand and the style your logo design should communicate.

```html
<!DOCTYPE html>
<html lang="en">
<head>
<meta charset="utf-8">
<title>Style Guide</title>
<link href="https://fonts.googleapis.com/css2?family=Mulish:wght@400;600;700&family=Lato:wght@400;700&display=swap" rel="stylesheet">
<style>
:root{
  --bg:#e6e6e6;--panel:#fff;--line:#cfcfcf;--ink:#444;--muted:#666;--tag:#7ea6d6;
  --warn:#d08a3c;--err:#c0333a;--ok:#3d8a3a;
  --blue1:#4276d8;--blue2:#2451b5;--teal1:#52b6d4;--teal2:#2f93b5;
  --dark1:#4a4a4a;--dark2:#222;--red1:#e0504e;--red2:#b92e2f;
  --green1:#6bbd5e;--green2:#3f9a3b;--rust1:#d97a3c;--rust2:#b85a22;
  --orange1:#ff9a1a;--orange2:#f07d00;
}
*{box-sizing:border-box;margin:0;padding:0}
html,body{width:1152px;height:1200px;overflow:hidden;background:var(--bg)}
.sheet{position:relative;width:1200px;height:1250px;transform:scale(.96);transform-origin:0 0;font-family:"Mulish",sans-serif;color:var(--ink)}
.abs{position:absolute}
.type-scale{left:78px;top:48px;display:flex;align-items:baseline;gap:0;white-space:nowrap}
.type-scale .tag{color:var(--tag);margin-right:18px}
.type-scale .item{margin-right:26px;color:#555}
.rule{left:38px;top:113px;width:1124px;height:1px;background:#aaa}
.section-title{font-size:25px;color:#444;font-weight:400}
.panel{background:var(--panel);border:1px solid var(--line)}
.label{font-size:14.5px;text-align:right;color:#444}
.field{height:36px;border:1px solid #ccc;border-radius:3px;background:#fff}
.help{font-family:"Lato",sans-serif;font-size:13px}
.warn{color:var(--warn)}.err{color:var(--err)}.ok{color:var(--ok)}
.opt{font-size:14.5px;line-height:20px;color:#444}
.box{width:14px;height:14px;border:1px solid #aaa;background:#fff}
.radio{width:15px;height:15px;border:1px solid #aaa;border-radius:50%;background:#fff}
.alert{left:63px;width:524px;border:1px solid;border-radius:3px;padding:10px 12px;font-size:14.5px;line-height:20px}
.alert .x{position:absolute;right:12px;top:6px;color:#aaa;font-size:16px}
.a-ok{background:#dff0d8;border-color:#cfe6c4;color:#3c763d}
.a-info{background:#d9edf7;border-color:#bcdff0;color:#31708f}
.a-warn{background:#fcf8e3;border-color:#f5e8c0;color:#c0883a}
.a-err{background:#f2dede;border-color:#ebcccc;color:#b94a48}
.btn{display:flex;align-items:center;justify-content:center;border-radius:3px;color:#fff;font-family:"Mulish",sans-serif}
.big{font-size:20px;letter-spacing:.5px}
.small{font-size:14px;font-weight:600}
.light{background:linear-gradient(#fbfbfb,#e4e4e4);border:1px solid #c8c8c8;color:#444}
.blue{background:linear-gradient(var(--blue1),var(--blue2))}
.teal{background:linear-gradient(var(--teal1),var(--teal2))}
.dark{background:linear-gradient(var(--dark1),var(--dark2))}
.red{background:linear-gradient(var(--red1),var(--red2))}
.green{background:linear-gradient(var(--green1),var(--green2))}
.rust{background:linear-gradient(var(--rust1),var(--rust2))}
.orange{background:linear-gradient(var(--orange1),var(--orange2))}
</style>
</head>
<body>
<div class="sheet">
  <div class="abs type-scale">
    <span class="tag" style="font-size:29px">&lt;h1&gt;</span><span class="item" style="font-size:31px">Page Title</span>
    <span class="tag" style="font-size:21px">&lt;h2&gt;</span><span class="item" style="font-size:24px">Page Subtitle</span>
    <span class="tag" style="font-size:18px">&lt;h3&gt;</span><span class="item" style="font-size:20px">Page Subtitle</span>
    <span class="tag" style="font-size:16px">&lt;h4&gt;</span><span class="item" style="font-size:16.5px">Page Subtitle</span>
    <span class="tag" style="font-size:16px">&lt;p&gt;</span><span class="item" style="font-size:14.5px">Normal Text</span>
  </div>
  <div class="abs rule"></div>

  <h2 class="abs section-title" style="left:50px;top:142px">Common elements</h2>
  <div class="abs panel" style="left:50px;top:176px;width:1100px;height:472px"></div>

  <div class="abs label" style="left:60px;width:162px;top:219px">Text input</div>
  <div class="abs field" style="left:241px;top:209px;width:264px"></div>

  <div class="abs label warn" style="left:60px;width:162px;top:275px">Input with warning</div>
  <div class="abs field" style="left:241px;top:265px;width:264px;border-color:var(--warn)"></div>
  <div class="abs help warn" style="left:247px;top:302px">Something may have gone wrong</div>

  <div class="abs label err" style="left:60px;width:162px;top:357px">Input with error</div>
  <div class="abs field" style="left:241px;top:347px;width:264px;border-color:var(--err)"></div>
  <div class="abs help err" style="left:247px;top:385px">Please correct the error</div>

  <div class="abs label ok" style="left:60px;width:162px;top:438px">Input with success</div>
  <div class="abs field" style="left:241px;top:428px;width:264px;border-color:var(--ok)"></div>
  <div class="abs help ok" style="left:247px;top:465px">Woohoo!</div>

  <div class="abs label" style="left:60px;width:162px;top:518px">Auto suggest</div>
  <div class="abs field" style="left:241px;top:508px;width:264px;border-color:#e9a24a"></div>
  <div class="abs help" style="left:241px;top:548px;line-height:22px;color:#444">In addition to freeform text, any HTML<br>text-based input appears like so.</div>

  <div class="abs label" style="left:580px;width:138px;top:221px">Select list</div>
  <div class="abs field" style="left:733px;top:209px;width:355px;background:linear-gradient(#fafafa,#e6e6e6);font-size:14.5px;padding:10px 15px">Something
    <svg class="abs" style="right:12px;top:13px" width="14" height="9"><path d="M0 0h14L7 9z" fill="#444"/></svg></div>

  <div class="abs label" style="left:580px;width:138px;top:268px">Select list</div>
  <div class="abs field" style="left:733px;top:258px;width:355px;font-size:14.5px;padding:10px 10px">something
    <div class="abs" style="left:314px;top:0;width:40px;height:34px;border-left:1px solid #ccc;background:linear-gradient(#fafafa,#e6e6e6)"></div>
    <svg class="abs" style="right:12px;top:13px" width="14" height="9"><path d="M0 0h14L7 9z" fill="#444"/></svg></div>

  <div class="abs label" style="left:580px;width:138px;top:315px">Checkbox</div>
  <div class="abs box" style="left:734px;top:316px"></div>
  <div class="abs opt" style="left:755px;top:314px">Option one is this and that–be sure to include<br>why it's great</div>

  <div class="abs label" style="left:580px;width:138px;top:375px">Radio buttons</div>
  <div class="abs radio" style="left:733px;top:377px"><div style="width:7px;height:7px;border-radius:50%;background:var(--blue1);margin:3px"></div></div>
  <div class="abs opt" style="left:755px;top:374px">Option one is this and that–be sure to include<br>why it's great</div>
  <div class="abs radio" style="left:733px;top:437px"></div>
  <div class="abs opt" style="left:755px;top:434px">Option two can is something else and selecting it<br>will deselect option one</div>

  <div class="abs label" style="left:580px;width:138px;top:495px">Checkboxes</div>
  <div class="abs box" style="left:734px;top:497px"></div><div class="abs opt" style="left:755px;top:494px">1</div>
  <div class="abs box" style="left:776px;top:497px"></div><div class="abs opt" style="left:795px;top:494px">2</div>
  <div class="abs box" style="left:820px;top:497px"></div><div class="abs opt" style="left:838px;top:494px">3</div>

  <div class="abs label" style="left:580px;width:138px;top:535px">Textarea</div>
  <div class="abs field" style="left:733px;top:540px;width:354px;height:87px">
    <svg class="abs" style="right:3px;bottom:3px" width="10" height="10"><path d="M9 2L2 9M9 6L6 9" stroke="#999"/></svg></div>

  <h2 class="abs section-title" style="left:49px;top:683px">Notification</h2>
  <div class="abs panel" style="left:50px;top:717px;width:548px;height:478px"></div>

  <div class="abs alert a-ok" style="top:733px;height:37px;padding-top:8px"><b>Well done!</b> You successfully read this important message.<span class="x">×</span></div>
  <div class="abs alert a-info" style="top:790px;height:57px;padding-top:8px"><b>Heads up!</b> This alert needs your attention, but it's not super<br>important.<span class="x">×</span></div>
  <div class="abs alert a-warn" style="top:867px;height:57px;padding-top:8px"><b>Warning!</b><br>Best check you self,, you're not...<span class="x">×</span></div>
  <div class="abs alert a-err" style="top:944px;height:56px;padding-top:8px"><b>Oh snap!</b><br>Change a few things up and try submitting again.<span class="x">×</span></div>
  <div class="abs alert a-err" style="top:1021px;height:157px;padding-top:8px"><b>Oh snap! You got an error!</b><span class="x">×</span>
    <p style="font-family:Lato,sans-serif;font-size:14px;line-height:23px;color:#333;margin-top:2px">Change this and that and try again. Lorem Ipsum is simply dummy<br>text of the printing and typesetting industry. Lorem Ipsum has<br>been the industry's standard dummy text ever since the</p>
  </div>
  <div class="abs btn blue" style="left:76px;top:1131px;width:150px;height:35px;font-size:14.5px;font-weight:600">Take this action</div>
  <div class="abs btn light" style="left:236px;top:1131px;width:100px;height:35px;font-size:14.5px">Cancel</div>

  <h2 class="abs section-title" style="left:617px;top:683px">Button</h2>
  <div class="abs panel" style="left:618px;top:717px;width:536px;height:478px"></div>

  <div class="abs btn orange" style="left:637px;top:736px;width:312px;height:47px;justify-content:flex-start;padding-left:18px;font-size:18px;font-weight:700">PRICE LEVEL
    <svg class="abs" style="right:16px;top:18px" width="14" height="9"><path d="M0 0h14L7 9z" fill="#fff"/></svg></div>
  <div class="abs btn blue big" style="left:637px;top:799px;width:312px;height:47px;border-bottom:2px solid #1a3a8a">SEARCH QUOTES</div>

  <div class="abs btn light big" style="left:637px;top:864px;width:162px;height:45px">BUTTON</div>
  <div class="abs btn blue big" style="left:809px;top:864px;width:162px;height:45px">BUTTON</div>
  <div class="abs btn teal big" style="left:980px;top:864px;width:162px;height:45px">BUTTON</div>
  <div class="abs btn dark big" style="left:637px;top:925px;width:162px;height:45px">BUTTON</div>
  <div class="abs btn red big" style="left:809px;top:925px;width:162px;height:45px">BUTTON</div>
  <div class="abs btn green big" style="left:980px;top:925px;width:162px;height:45px">BUTTON</div>

  <div class="abs btn light small" style="left:637px;top:995px;width:112px;height:35px;font-weight:400">Button</div>
  <div class="abs btn blue small" style="left:759px;top:995px;width:112px;height:35px">Button</div>
  <div class="abs btn teal small" style="left:881px;top:995px;width:112px;height:35px">Button</div>
  <div class="abs btn dark small" style="left:1005px;top:995px;width:112px;height:35px">Button</div>
  <div class="abs btn red small" style="left:637px;top:1043px;width:112px;height:35px">Button</div>
  <div class="abs btn green small" style="left:759px;top:1043px;width:112px;height:35px">Button</div>
  <div class="abs btn rust small" style="left:881px;top:1043px;width:112px;height:35px">Button</div>
  <div class="abs btn orange small" style="left:1005px;top:1043px;width:112px;height:35px">Button</div>
</div>
</body>
</html>
```